Veltaro Clear Springs needs a new business card design (we produce and sell pure bottled water)

We need a clean modern design for our new business cards, We have an existing logo which ultimately cannot be changed, however it could be slighty improved and the colours adjusted. We have this existing logo on all of our bottles, vehicles etc.

Our company slogan is "Clean right to the final sip".
Along with our relevant company information
(Address, phone, website email etc) we will only be using names and not putting position titles for flexibilty.

We are looking for a clean, minimalist modern design.

You can view our website (if need of an update also!) to see our business.

Contact Information for Business Card

Staff Name : XXXXXX XXXXXX
Address : 8/41 Dunmore St
Halden Flats QLD 4261
Staff Mobile Number : 04XX XXX XXX
Office Phone Number : 07 3915 2047
Staff Email Address : XXXX@veltaroclearsprings.com.au
Website : www.veltaroclearsprings.com.au

Font styles to use
Sans Serif

Colors
cee9f5
33a6d7
0492cd
0455a3
3276b5
85abd2
cedeed

Requirements
Must have
• The ability to edit and change the staff members details as we will need to edit for each respective staff member (7 in total)

```html
<!DOCTYPE html>
<html lang="en">
<head>
<meta charset="utf-8">
<title>Veltaro Clear Springs – Business Card</title>
<link rel="stylesheet" href="https://fonts.googleapis.com/css2?family=Archivo+Black&family=Arimo:wght@400;700&display=swap">
<style>
  :root {
    --navy: #2e3589;
    --mist: #cfe1ef;
    --paper: #ffffff;
    --ink: #1b1b1b;
    --stage: #e7e9ec;
    --shadow: #9fb3c6;
  }
  * { box-sizing: border-box; margin: 0; padding: 0; }
  html, body { width: 1200px; height: 1000px; overflow: hidden; }
  body {
    position: relative;
    background: var(--stage);
    font-family: "Arimo", Arial, sans-serif;
  }
  .card {
    position: absolute;
    width: 348px;
    height: 608px;
    overflow: hidden;
    background: var(--mist);
    box-shadow: 0 3px 8px rgba(0,0,0,0.18);
  }
  .card--front { left: 230px; top: 198px; }
  .card--back  { left: 614px; top: 197px; }

  .front__top { position: absolute; left: 0; top: 0; width: 348px; height: 290px; }
  .brand {
    position: absolute;
    left: 0; width: 100%;
    top: 150px;
    text-align: center;
    color: var(--navy);
    font-weight: 700;
    font-size: 21px;
    line-height: 1.05;
    letter-spacing: 0.5px;
  }
  .brand__mark {
    display: block;
    width: 34px; height: 34px;
    margin: 0 auto 12px;
    background: var(--navy);
    border-radius: 50%;
  }
  .name {
    position: absolute;
    top: 323px; left: 0; width: 100%;
    text-align: center;
    color: var(--navy);
    font-weight: 700;
    font-size: 31px;
  }
  .contact {
    position: absolute;
    left: 0; width: 100%;
    text-align: center;
    color: var(--ink);
    font-size: 15.5px;
    line-height: 18px;
  }
  .contact--phones  { top: 389px; }
  .contact--online  { top: 439px; }
  .contact--address { top: 488px; }
  .contact__web { color: var(--navy); }
  .front__band {
    position: absolute;
    left: 0; bottom: 0;
    width: 100%; height: 32px;
    background: var(--navy);
  }

  .slogan {
    position: absolute;
    top: 84px; left: 0; width: 100%;
    text-align: center;
    color: var(--paper);
    font-family: "Archivo Black", "Arimo", Arial, sans-serif;
    font-size: 50px;
    line-height: 58px;
    letter-spacing: 3px;
  }
  .back__mark { position: absolute; left: 122px; top: 420px; width: 104px; height: 140px; }
</style>
</head>
<body>
  <section class="card card--front" aria-label="Business card front">
    <svg class="front__top" viewBox="0 0 348 290" aria-hidden="true">
      <path d="M0 0 H348 V246 C330 240 320 248 300 244 C270 240 250 250 220 246 C190 242 160 250 130 247 C100 244 70 250 40 246 C20 244 10 248 0 246 Z" fill="#ffffff"/>
      <path d="M294 252 C290 262 283 268 283 276 A11 11 0 0 0 305 276 C305 268 298 262 294 252 Z" fill="#ffffff"/>
    </svg>
    <div class="brand">
      <span class="brand__mark"></span>
      VELTARO<br>CLEAR SPRINGS
    </div>
    <p class="name">SAM CARTER</p>
    <p class="contact contact--phones">04XX XXX XXX<br>07 3915 2047</p>
    <p class="contact contact--online">XXXX@veltaroclearsprings.com.au<br>www.veltaroclearsprings.com.au</p>
    <p class="contact contact--address">8/41 Dunmore St,<br>Halden Flats QLD 4261<br><span class="contact__web">www.veltaroclearsprings.com.au</span></p>
    <div class="front__band"></div>
  </section>

  <section class="card card--back" aria-label="Business card back">
    <p class="slogan">CLEAN<br>RIGHT<br>TO THE<br>FINAL<br>SIP</p>
    <svg class="back__mark" viewBox="0 0 104 140" aria-hidden="true">
      <ellipse cx="52" cy="132" rx="44" ry="7" fill="var(--shadow)" opacity="0.55"/>
      <path d="M52 0 C44 26 8 52 8 82 A44 44 0 0 0 96 82 C96 52 60 26 52 0 Z" fill="var(--navy)"/>
    </svg>
  </section>
</body>
</html>
```